Startup Biz for Seniors needs your help!

Our business is a Startup that Employs Caregivers to do IN HOME Care of the Elderly. Our website is not yet running. But, a business similar to ours is Tallbrookcare.com

We are looking for a card that only has 4 Elements:
-Logo
- Website
- Tag Line
- Phone
We would like to see some eye catching backgrounds.
We would like to see some designs with and some without a Photo.
Would like the Photo to be of a Caregiver taking care of a Senior. The photo should show both of them smiling.

Target Market(s)

Age 35-55 who has Parents that are Elderly and need care

Industry/Entity Type

Home Health Care

Contact Information for Business Card

Want it to Pop Out to the viewer . Thinking maybe:
Side 1: LOGO with Website & Tag line
Side 2: Phone Number

Font styles to use
Other font styles liked:
• Same Font as our Logo

Colors

Designer to choose colors to be used in the design.

Requirements
Must have
• Logo, website, Tag Line, Phone number and Email: "info@velvetdays.example"
• Please use one of the photos that I have attached.
Nice to have
• Would like to see a Photo worked in that has a Care Taker taking care of an Elderly Person and they are both smiling.

```html
<!DOCTYPE html>
<html lang="en">
<head>
<meta charset="utf-8">
<title>VelvetDays.example – Business Card</title>
<link href="https://fonts.googleapis.com/css2?family=Ubuntu:wght@500;700&display=swap" rel="stylesheet">
<style>
  :root {
    --bg: #e6e7ea;
    --card: #ffffff;
    --orange: #e64d1c;
    --blue: #1f4fa3;
    --ink: #1c1c1c;
    --leaf-light: #b9dc8a;
    --leaf-dark: #4f8a2c;
    --soft: #f6d9cb;
  }
  * { margin: 0; padding: 0; box-sizing: border-box; }
  html, body { width: 1200px; height: 1000px; overflow: hidden; background: var(--bg); }
  .canvas { position: relative; width: 1200px; height: 1000px; }

  .card {
    position: absolute;
    left: 320px;
    width: 560px;
    height: 320px;
    border-radius: 18px;
    overflow: hidden;
    background: var(--card);
    box-shadow: 0 10px 28px rgba(0,0,0,.18);
  }
  .card--front { top: 130px; }
  .card--back  { top: 540px; }

  .band { position: absolute; left: 0; bottom: 0; width: 560px; height: 80px; display: block; }

  /* brand block */
  .brand { position: absolute; left: 34px; top: 30px; }
  .brand__row { display: flex; align-items: center; gap: 14px; }
  .brand__dot { width: 58px; height: 58px; border-radius: 50%; background: var(--orange); flex: none; }
  .brand__name {
    font-family: "Ubuntu", sans-serif; font-weight: 700;
    font-size: 34px; color: var(--blue); letter-spacing: -.5px;
  }
  .tagline {
    font-family: "Ubuntu", sans-serif; font-weight: 500; font-size: 17px;
    color: var(--blue); margin: 2px 0 0 72px;
  }

  /* contact block */
  .contact { position: absolute; left: 40px; top: 136px; font-family: "Ubuntu", sans-serif; color: var(--ink); }
  .contact__line { display: flex; align-items: center; gap: 10px; height: 34px; }
  .contact__icon { width: 24px; height: 24px; flex: none; }
  .contact__phone { font-size: 27px; font-weight: 700; }
  .contact__text { font-size: 22px; font-weight: 500; }
  .contact__web { padding-left: 34px; }

  .accent-circle {
    position: absolute; right: 40px; bottom: 40px;
    width: 140px; height: 140px; border-radius: 50%;
    background: var(--soft); opacity: .55;
  }

  /* photo side */
  .photo {
    position: absolute; inset: 0;
    background: radial-gradient(ellipse at 72% 62%, #f2f0ee 0 22%, transparent 40%),
                linear-gradient(135deg, var(--leaf-light) 0%, #8cc45d 45%, var(--leaf-dark) 100%);
  }
  .card--back .brand { top: 40px; left: 40px; }
</style>
</head>
<body>
<main class="canvas">

  <!-- Side 1: contact side -->
  <section class="card card--front">
    <div class="accent-circle" aria-hidden="true"></div>

    <div class="brand">
      <div class="brand__row">
        <span class="brand__dot" aria-hidden="true"></span>
        <span class="brand__name">VelvetDays.example</span>
      </div>
      <p class="tagline">Gentle Care, Right at Home</p>
    </div>

    <div class="contact">
      <div class="contact__line">
        <svg class="contact__icon" viewBox="0 0 24 24" aria-hidden="true">
          <circle cx="12" cy="12" r="11" fill="none" stroke="var(--orange)" stroke-width="2"/>
          <path d="M9 6.5c-1.2.6-1.6 2-1 3.6 1 2.8 3 5 5.6 6.6 1.4.8 2.8.6 3.6-.6l-2.2-2-1.4.8c-1.4-.8-2.6-2.2-3.2-3.6l1-1.2z" fill="var(--orange)"/>
        </svg>
        <span class="contact__phone">1.800.555.0142</span>
      </div>
      <div class="contact__line">
        <svg class="contact__icon" viewBox="0 0 24 24" aria-hidden="true">
          <rect x="2" y="5" width="20" height="14" fill="none" stroke="var(--orange)" stroke-width="2"/>
          <path d="M2 5l10 8 10-8M2 19l7-6M22 19l-7-6" fill="none" stroke="var(--orange)" stroke-width="2"/>
        </svg>
        <span class="contact__text">info@velvetdays.example</span>
      </div>
      <div class="contact__line contact__web">
        <span class="contact__text">velvetdays.example</span>
      </div>
    </div>

    <svg class="band" viewBox="0 0 560 80" preserveAspectRatio="none" aria-hidden="true">
      <path d="M0 38 H44 L56 22 H86 L98 38 H560 V80 H0 Z" fill="var(--orange)"/>
    </svg>
  </section>

  <!-- Side 2: photo side -->
  <section class="card card--back">
    <div class="photo" role="img" aria-label="Photo of a smiling caregiver with her arm around a smiling senior woman, green garden foliage behind"></div>

    <div class="brand">
      <div class="brand__row">
        <span class="brand__dot" aria-hidden="true"></span>
        <span class="brand__name">VelvetDays.example</span>
      </div>
      <p class="tagline">Gentle Care, Right at Home</p>
    </div>

    <svg class="band" viewBox="0 0 560 80" preserveAspectRatio="none" aria-hidden="true">
      <path d="M0 44 H44 L56 28 H86 L98 44 H560 V80 H0 Z" fill="var(--blue)"/>
    </svg>
  </section>

</main>
</body>
</html>
```